KRT World Class Organisation Poster

We are looking for ideas on how to design this poster to best capture the message we are trying to convey (KRT World Class Organisation). Make sure that these 5 statements feature on the poster.

Logo has been provided, please include in your poster design.

Please use the logo design as the inspiration for your poster layout, drawing on the DNA double helix symbol.

Also refer to the layout of the attached poster. We would like to retain the layout however it should be visually appealing - use your imagination & creativity!
Updates

Updated design brief & extended deadline.

Target Market(s)

internal company use only - logo provided which will need to be included.

Requirements
Must have
• The poster should be in portrait format as it will be printed in 'A3' size.

Must include the KRT logo provided - see attached file.
Nice to have
• Please use the logo design as the inspiration for your poster layout, drawing on the DNA double helix symbol.

```html
<!DOCTYPE html>
<html lang="en">
<head>
<meta charset="utf-8">
<title>World Class Organisation</title>
<link rel="stylesheet" href="https://fonts.googleapis.com/css2?family=Montserrat:wght@800&family=Didact+Gothic&display=swap">
<style>
  :root {
    --frame-grey: #8f8a8c;
    --crimson: #7a0f14;
    --crimson-deep: #3d070a;
    --panel: #262424;
    --ink-white: #ffffff;
    --ink-silver: #cfcfcf;
    --ink-steel: #a9a9a9;
    --ornament: #e8e8e8;
  }
  html, body {
    margin: 0;
    padding: 0;
    width: 847px;
    height: 1200px;
    overflow: hidden;
    background: var(--frame-grey);
  }
  .poster {
    position: relative;
    width: 847px;
    height: 1200px;
    background:
      radial-gradient(ellipse at 50% 45%, transparent 55%, rgba(160,155,158,0.55) 100%),
      radial-gradient(ellipse at 40% 40%, var(--crimson) 0%, #5e0b10 55%, var(--crimson-deep) 100%);
    overflow: hidden;
  }
  .statement-panel {
    position: absolute;
    left: 90px;
    top: 98px;
    width: 670px;
    height: 994px;
    background: var(--panel);
    box-shadow: 0 0 18px rgba(0,0,0,0.45);
  }
  .statements {
    position: absolute;
    left: 0;
    top: 0;
  }
  .bold { font-family: "Montserrat", sans-serif; font-weight: 800; fill: var(--ink-white); }
  .light { font-family: "Didact Gothic", sans-serif; fill: var(--ink-white); }
  .light.silver { fill: var(--ink-silver); }
  .light.steel { fill: var(--ink-steel); }
  .headline { font-family: "Montserrat", sans-serif; font-weight: 800; fill: url(#silverSheen); }
  .flourish {
    position: absolute;
    left: 50%;
    width: 130px;
    height: 16px;
    margin-left: -65px;
    border-radius: 8px;
    background: linear-gradient(90deg, transparent, var(--ornament) 30%, var(--ornament) 70%, transparent);
    opacity: 0.55;
  }
  .flourish.top { top: 136px; }
  .flourish.bottom { top: 1006px; }
</style>
</head>
<body>
<main class="poster">
  <div class="statement-panel"></div>
  <div class="flourish top" role="img" aria-label="Decorative scroll flourish"></div>

  <svg class="statements" width="847" height="1200" viewBox="0 0 847 1200" aria-label="World class organisation statements">
    <defs>
      <linearGradient id="silverSheen" x1="0" y1="0" x2="0" y2="1">
        <stop offset="0" stop-color="#ffffff"/>
        <stop offset="1" stop-color="#9a9a9a"/>
      </linearGradient>
    </defs>
    <g text-anchor="middle">
      <text class="bold" x="423.5" y="198" font-size="24" textLength="614" lengthAdjust="spacingAndGlyphs">WE EMPLOY WORLD CLASS BUSINESS SYSTEMS</text>
      <text class="light" x="423.5" y="229" font-size="24" textLength="614" lengthAdjust="spacingAndGlyphs">TO EXCEED EXPECTATIONS BY DRIVING INNOVATION</text>
      <text class="light" x="423.5" y="265" font-size="32" textLength="614" lengthAdjust="spacingAndGlyphs">AT THE FOREFRONT OF TECHNOLOGY.</text>

      <text class="bold" x="423.5" y="326" font-size="30" textLength="614" lengthAdjust="spacingAndGlyphs">WE MANUFACTURE USING INNOVATIVE</text>
      <text class="bold" x="423.5" y="357" font-size="28" textLength="614" lengthAdjust="spacingAndGlyphs">WORLD CLASS MANUFACTURING PROCESSES</text>
      <text class="light" x="423.5" y="388" font-size="22" textLength="614" lengthAdjust="spacingAndGlyphs">AND LEAN TECHNOLOGIES ADAPTED TO PRODUCE SAFE,</text>
      <text class="light" x="423.5" y="418" font-size="19" textLength="614" lengthAdjust="spacingAndGlyphs">EFFECTIVE &amp; RELIABLE PRODUCTS TO MEET OUR PATIENTS’ NEEDS.</text>

      <text class="headline" x="423.5" y="505" font-size="76" textLength="614" lengthAdjust="spacingAndGlyphs">WE STRIVE TO BE</text>
      <text class="headline" x="423.5" y="553" font-size="46" textLength="614" lengthAdjust="spacingAndGlyphs">WORLD CLASS COLLEAGUES</text>
      <text class="light" x="423.5" y="585" font-size="21" textLength="614" lengthAdjust="spacingAndGlyphs">WHO ARE PROFESSIONAL, MOTIVATED, HELPFUL AND POSITIVE.</text>
      <text class="light silver" x="423.5" y="621" font-size="25" textLength="614" lengthAdjust="spacingAndGlyphs">WE ARE ACCOUNTABLE IN ACHIEVING OUR GOALS.</text>
      <text class="light silver" x="423.5" y="656" font-size="28" textLength="614" lengthAdjust="spacingAndGlyphs">WE ARE INNOVATIVE, ALWAYS CHALLENGE THE</text>
      <text class="light steel" x="423.5" y="691" font-size="31" textLength="614" lengthAdjust="spacingAndGlyphs">STATUS-QUO AND OPEN TO NEW IDEAS.</text>

      <text class="bold" x="423.5" y="757" font-size="22" textLength="614" lengthAdjust="spacingAndGlyphs">WE WORK WITH WORLD CLASS SERVICE PROVIDERS</text>
      <text class="light" x="423.5" y="792" font-size="34" textLength="614" lengthAdjust="spacingAndGlyphs">WHO ARE LEADERS AND INNOVATORS</text>
      <text class="light" x="423.5" y="823" font-size="25" textLength="614" lengthAdjust="spacingAndGlyphs">THAT CHALLENGE THE STATUS-QUO AND FOCUS ON</text>
      <text class="light" x="423.5" y="856" font-size="24" textLength="614" lengthAdjust="spacingAndGlyphs">QUALITY EXCELLENCE AND CONTINUOUS IMPROVEMENT</text>
      <text class="light" x="423.5" y="895" font-size="33" textLength="614" lengthAdjust="spacingAndGlyphs">TO EXCEED CUSTOMER EXPECTATIONS.</text>

      <text class="bold" x="423.5" y="955" font-size="24" textLength="614" lengthAdjust="spacingAndGlyphs">WE BELIEVE WORLD CLASS CUSTOMER SERVICE</text>
      <text class="light" x="423.5" y="983" font-size="18" textLength="614" lengthAdjust="spacingAndGlyphs">IS TO DELIVER THE ULTIMATE CUSTOMER SATISFACTION EVERY TIME.</text>
    </g>
  </svg>

  <div class="flourish bottom" role="img" aria-label="Decorative scroll flourish"></div>
</main>
</body>
</html>
```